BOLD & MINIMALIST DESIGN NEEDED

We want a very bold but minimalistic business card design that is impactful and utilizes both sides of the business card. Our current logo is included for your use.

We want bold fonts and good use of negative space. We don't want the logo to overpower the design.

Target Market(s)

Professionals who are building new commercial buildings.

Industry/Entity Type

Construction

Contact Information for Business Card

Name, Title, email, office phone, cell phone, website

Font styles to use
Serif
Sans Serif

Requirements
Must have
• Bold design!

```html
<!DOCTYPE html>
<html lang="en">
<head>
<meta charset="utf-8">
<title>Ridgeline Build — Business Card</title>
<link href="https://fonts.googleapis.com/css2?family=Oswald:wght@500;700&family=Montserrat:wght@400;500&display=swap" rel="stylesheet">
<style>
  :root {
    --backdrop: #3b3b3d;
    --card: #ffffff;
    --ink: #0c0c0c;
    --lime: #84c225;
    --text: #1a1a1a;
  }
  * { margin: 0; padding: 0; box-sizing: border-box; }
  html, body { width: 1200px; height: 675px; overflow: hidden; }
  body {
    background: var(--backdrop);
    position: relative;
    font-family: "Montserrat", sans-serif;
    color: var(--text);
  }
  .card {
    position: absolute;
    top: 244px;
    width: 329px;
    height: 187px;
    background: var(--card);
    border-radius: 12px;
    overflow: hidden;
  }
  .card--front { left: 267px; }
  .card--back { left: 604px; }

  .company-name {
    position: absolute;
    font-family: "Oswald", sans-serif;
    font-weight: 700;
    color: var(--ink);
    line-height: 1;
    white-space: nowrap;
    letter-spacing: 0.3px;
  }
  .card--front .company-name { left: 16px; top: 52px; font-size: 16px; }
  .card--back .company-name {
    left: 112px; width: 217px; top: 82px;
    font-size: 22px; text-align: center;
  }

  .accent-tab {
    position: absolute;
    left: 0; top: 103px;
    width: 4px; height: 23px;
    background: var(--lime);
    border-radius: 0 3px 3px 0;
  }
  .person {
    position: absolute;
    left: 16px; top: 100px;
  }
  .person__name {
    font-family: "Oswald", sans-serif;
    font-weight: 500;
    font-size: 17px;
    color: var(--lime);
    letter-spacing: 0.2px;
    line-height: 1.1;
  }
  .person__role {
    font-size: 7.5px;
    font-weight: 500;
    letter-spacing: 0.4px;
    margin-top: 1px;
  }
  .contact {
    position: absolute;
    left: 16px; top: 134px;
    list-style: none;
    font-size: 7.4px;
    line-height: 9.8px;
  }
  .contact li { display: flex; align-items: center; gap: 3px; }
  .contact svg { width: 7px; height: 7px; flex: none; }
  .contact .hl { color: var(--lime); }

  .block {
    position: absolute;
    background: var(--ink);
  }
  .card--front .block { right: 0; top: 45px; width: 102px; height: 142px; }
  .card--back .block { left: 0; top: 0; width: 102px; height: 187px; }
</style>
</head>
<body>
  <section class="card card--front">
    <p class="company-name">RIDGELINE BUILD</p>

    <span class="accent-tab"></span>
    <div class="person">
      <p class="person__name">MARA ELLISON</p>
      <p class="person__role">OWNER</p>
    </div>

    <ul class="contact">
      <li>
        <svg viewBox="0 0 10 10"><path fill="#84c225" d="M2 0.5l1.8 2-1 1.2a6 6 0 0 0 3.5 3.5l1.2-1 2 1.8-1.2 1.5C4.5 9.5 0.5 5.5 0.5 1.7z"/></svg>
        (555) 214-7730
      </li>
      <li>
        <svg viewBox="0 0 10 10"><rect x="2.5" y="0.5" width="5" height="9" rx="1" fill="none" stroke="#84c225" stroke-width="1.2"/><circle cx="5" cy="7.8" r="0.6" fill="#84c225"/></svg>
        (555) 214-7730
      </li>
      <li>
        <svg viewBox="0 0 10 10"><rect x="0.6" y="2" width="8.8" height="6" fill="none" stroke="#84c225" stroke-width="1"/><path d="M0.8 2.3L5 5.5 9.2 2.3" fill="none" stroke="#84c225" stroke-width="1"/></svg>
        ridgelinestudio@mail.com
      </li>
      <li>
        <svg viewBox="0 0 10 10"><circle cx="5" cy="5" r="4.3" fill="none" stroke="#84c225" stroke-width="1"/><ellipse cx="5" cy="5" rx="1.8" ry="4.3" fill="none" stroke="#84c225" stroke-width="0.8"/><path d="M0.7 5h8.6" stroke="#84c225" stroke-width="0.8"/></svg>
        <span>www.<span class="hl">ridgelinestudio</span>.com</span>
      </li>
    </ul>

    <div class="block" aria-hidden="true"></div>
  </section>

  <section class="card card--back">
    <div class="block" aria-hidden="true"></div>
    <p class="company-name">RIDGELINE BUILD</p>
  </section>
</body>
</html>
```